Self Storage Company Needs Postcard Design & Flyer Needed

The name of our company is Tidy Locker Yard. We are going to be opening two brand new locations. I need a postcard designed that we will mail to several thousand addresses near our new locations. The postcard needs to announce the opening of our new locations and our special promotion.
I need to have a postcard design that is catchy and worded in a way that will get people to stop by the stores and when they do they will select a key and if that key opens the lock then they will win 3 months of free storage.
1. NOW OPEN! UNLOCK FREE RENT TODAY.
2. Stop by one of our brand new locations and test your luck. Draw a key and if it opens the lock you win three months of free storage.
3. Hurry in, limited time only.
4. These locations need to be listed on postcard:
Tidy Locker Yard
24815 Marlow Court
Larkfield, IN 46901
317.555.4820
Tidy Locker Yard
16200 Quenby Glen Road
Brookvale, IN 46977
317-555-7136
5. website address: www.tidylockeryard.example
6. logo attached.
7. feel free to use any pixvault photos
8. I've attached a flyer that has amenities listed. Feel free to use as many as them as you would like.
I also need to have a 8.5" X 11" flyer designed to match the postcards that we will display in the offices.
Look and feel
Each slider illustrates characteristics of the customer's brand and the style your logo design should communicate.

```html
<!DOCTYPE html>
<html lang="en">
<head>
<meta charset="utf-8">
<title>Tidy Locker Yard – Grand Opening Postcard</title>
<link rel="stylesheet" href="https://fonts.googleapis.com/css2?family=Anton&family=Arimo:wght@400;700&family=Source+Sans+3:wght@400;700&display=swap">
<style>
  :root {
    --backdrop: #4a4b4d;
    --red: #e41e26;
    --red-deep: #c8161d;
    --yellow: #fff21f;
    --green: #00a14b;
    --green-deep: #0b5a2c;
    --white: #ffffff;
    --ink: #1d1d1b;
    --stamp: #e0e0dc;
    --rule: #333333;
  }
  * { margin: 0; padding: 0; box-sizing: border-box; }
  html, body { width: 937px; height: 1200px; overflow: hidden; background: var(--backdrop); }
  body { position: relative; font-family: "Source Sans 3", sans-serif; }

  .card { position: absolute; left: 72px; width: 807px; height: 522px; overflow: hidden; box-shadow: 0 2px 6px rgba(0,0,0,.35); }
  .card--front { top: 66px; }
  .card--back { top: 616px; background: var(--white); }
  .abs { position: absolute; }

  /* front */
  .warehouse-photo { inset: 0; background: linear-gradient(160deg, #6f7a84 0%, #b79a6e 35%, #d08a3a 55%, #4c6f9e 75%, #5a5f66 100%); }
  .brand-name { left: 128px; top: 64px; display: flex; align-items: center; gap: 10px; }
  .brand-name__mark { width: 22px; height: 22px; background: var(--yellow); }
  .brand-name__text { font-family: "Source Sans 3", sans-serif; font-weight: 700; font-size: 26px; color: var(--white); white-space: nowrap; }
  .headline-panel { left: 26px; top: 192px; width: 406px; height: 109px; background: var(--yellow); border-top-right-radius: 38px; }
  .headline { position: absolute; left: 44px; top: 4px; font-family: "Anton", sans-serif; font-weight: 400; color: var(--red); font-size: 64px; line-height: 1.15; letter-spacing: .5px; }
  .subhead { position: absolute; left: 46px; top: 80px; font-family: "Arimo", sans-serif; color: var(--red); font-size: 19px; letter-spacing: 1.2px; word-spacing: 3px; }
  .offer-panel { left: 26px; top: 301px; width: 260px; height: 208px; background: var(--green); color: var(--white); padding: 0 10px; }
  .offer-panel svg { display: block; margin: 12px auto 0 102px; }
  .offer-panel p { font-size: 16.5px; line-height: 21.5px; margin-top: 8px; white-space: nowrap; }
  .offer-panel p + p { margin-top: 9px; }
  .hurry-panel { left: 286px; top: 301px; width: 146px; height: 208px; background: var(--red); }
  .hurry-text { position: absolute; left: 50%; top: 50%; width: 208px; transform: translate(-50%, -50%) rotate(-90deg); color: var(--white); font-family: "Arimo", sans-serif; line-height: 1; padding-left: 8px; }
  .hurry-text strong { display: block; font-size: 40px; font-weight: 400; }
  .hurry-text span { display: block; font-size: 19px; margin-top: 6px; }
  .web-pill { left: 484px; top: 471px; width: 310px; height: 38px; background: var(--green); display: flex; align-items: center; padding-left: 8px; gap: 8px; color: var(--white); font-size: 16px; letter-spacing: 1.6px; }

  /* back */
  .message-side { left: 0; top: 0; width: 404px; height: 522px; background: linear-gradient(90deg, var(--red-deep), var(--red) 55%, #e8262c); }
  .intro { left: 13px; top: 22px; width: 380px; color: var(--white); font-size: 14.5px; line-height: 19px; }
  .feature-band { left: 0; top: 74px; width: 426px; height: 58px; background: var(--yellow); border-top: 3px solid var(--green); border-bottom: 3px solid var(--green); }
  .band-notch { left: 404px; top: 132px; }
  .band-name { left: 14px; top: 86px; width: 76px; font-family: "Source Sans 3", sans-serif; font-weight: 700; font-size: 14px; line-height: 17px; color: var(--ink); }
  .band-text { left: 97px; top: 84px; font-family: "Arimo", sans-serif; font-size: 15px; line-height: 20px; color: var(--ink); word-spacing: 2px; }
  .features-title { left: 52px; top: 138px; color: var(--white); font-size: 18.5px; font-weight: 400; }
  .feature-list { left: 17px; top: 175px; list-style: none; }
  .feature-list li { display: flex; align-items: center; height: 31.2px; color: var(--white); font-size: 13.5px; }
  .feature-list svg { margin-right: 16px; }
  .boxes-art { left: 288px; top: 168px; width: 108px; height: 260px; background: linear-gradient(180deg, #d7a86c, #c48e55); border-radius: 4px; }
  .call-bar { left: 0; top: 426px; width: 404px; height: 48px; background: var(--green-deep); }
  .call-bar svg { position: absolute; left: 0; top: 0; }
  .call-label { left: 24px; top: 436px; color: var(--white); font-family: "Arimo", sans-serif; font-size: 21px; word-spacing: 3px; }
  .call-number { left: 216px; top: 436px; color: var(--white); font-family: "Arimo", sans-serif; font-size: 22px; }
  .web-bar { left: 0; top: 474px; width: 404px; height: 48px; background: var(--yellow); display: flex; align-items: center; padding-left: 21px; gap: 11px; color: var(--ink); font-family: "Arimo", sans-serif; font-weight: 700; font-size: 15px; letter-spacing: 2px; }

  .stamp-box { left: 718px; top: 30px; width: 64px; height: 71px; background: var(--stamp); }
  .address-rule { left: 582px; width: 188px; height: 1px; background: var(--rule); }
  .location { top: 462px; color: var(--ink); }
  .location__name { font-size: 11.5px; line-height: 13px; }
  .location__street { font-size: 8px; line-height: 11px; white-space: nowrap; }
  .location__phone { display: flex; align-items: center; gap: 6px; font-size: 11.5px; margin-top: 3px; }
</style>
</head>
<body>

<section class="card card--front">
  <div class="abs warehouse-photo" role="img" aria-label="Photo of a warehouse with tall orange and blue pallet racks stacked with cardboard boxes"></div>

  <div class="abs brand-name">
    <span class="brand-name__mark"></span>
    <span class="brand-name__text">Tidy Locker Yard</span>
  </div>

  <div class="abs headline-panel">
    <h1 class="headline">NOW OPEN!</h1>
    <p class="subhead">UNLOCK FREE RENT TODAY.</p>
  </div>

  <div class="abs offer-panel">
    <svg width="54" height="58" viewBox="0 0 54 58" aria-hidden="true">
      <path d="M12 26 V16 a12 12 0 0 1 24 0 V26" fill="none" stroke="#b8b8b8" stroke-width="5"/>
      <rect x="4" y="24" width="40" height="32" rx="4" fill="#c9a24a"/>
      <circle cx="24" cy="38" r="4" fill="#5a4313"/>
      <rect x="30" y="34" width="22" height="6" rx="3" fill="#1d1d1b"/>
    </svg>
    <p>Stop by one of our brand new<br>locations and test your luck.</p>
    <p>Draw a key and if it opens<br>the lock you win three months<br>of free storage.</p>
  </div>

  <div class="abs hurry-panel">
    <div class="hurry-text"><strong>Hurry in</strong><span>limited time only.</span></div>
  </div>

  <div class="abs web-pill">
    <svg width="24" height="24" viewBox="0 0 24 24" aria-hidden="true" fill="none" stroke="#fff" stroke-width="1.6">
      <circle cx="12" cy="12" r="10"/><ellipse cx="12" cy="12" rx="4.5" ry="10"/><path d="M2 12h20M4 6.5h16M4 17.5h16"/>
    </svg>
    <span>www.tidylockeryard.example</span>
  </div>
</section>

<section class="card card--back">
  <div class="abs message-side"></div>
  <p class="abs intro">You will find <strong>Everything</strong> you could want in a Self Storage Facility at Tidy Locker Yard.</p>

  <div class="abs feature-band"></div>
  <svg class="abs band-notch" width="22" height="14" viewBox="0 0 22 14" aria-hidden="true"><path d="M0 0H22L0 14Z" fill="#0b5a2c"/></svg>
  <p class="abs band-name">Tidy Locker<br>Yard</p>
  <p class="abs band-text">We Offer the Most Current and<br>Innovative Features in the Industry.</p>

  <h2 class="abs features-title">Some Features :</h2>
  <ul class="abs feature-list">
    <li><svg width="19" height="19" viewBox="0 0 19 19" aria-hidden="true"><rect width="19" height="19" fill="#fff21f"/><path d="M4 10l4 4 8-9" fill="none" stroke="#00a14b" stroke-width="2.4"/></svg>Month - to - Month Lease</li>
    <li><svg width="19" height="19" viewBox="0 0 19 19" aria-hidden="true"><rect width="19" height="19" fill="#fff21f"/><path d="M4 10l4 4 8-9" fill="none" stroke="#00a14b" stroke-width="2.4"/></svg>Online Payments</li>
    <li><svg width="19" height="19" viewBox="0 0 19 19" aria-hidden="true"><rect width="19" height="19" fill="#fff21f"/><path d="M4 10l4 4 8-9" fill="none" stroke="#00a14b" stroke-width="2.4"/></svg>Gated Property Access</li>
    <li><svg width="19" height="19" viewBox="0 0 19 19" aria-hidden="true"><rect width="19" height="19" fill="#fff21f"/><path d="M4 10l4 4 8-9" fill="none" stroke="#00a14b" stroke-width="2.4"/></svg>24 Hour Vidoe Monitoring</li>
    <li><svg width="19" height="19" viewBox="0 0 19 19" aria-hidden="true"><rect width="19" height="19" fill="#fff21f"/><path d="M4 10l4 4 8-9" fill="none" stroke="#00a14b" stroke-width="2.4"/></svg>Convenient Loding Areas</li>
    <li><svg width="19" height="19" viewBox="0 0 19 19" aria-hidden="true"><rect width="19" height="19" fill="#fff21f"/><path d="M4 10l4 4 8-9" fill="none" stroke="#00a14b" stroke-width="2.4"/></svg>Discounted Pre - Pay Programs</li>
    <li><svg width="19" height="19" viewBox="0 0 19 19" aria-hidden="true"><rect width="19" height="19" fill="#fff21f"/><path d="M4 10l4 4 8-9" fill="none" stroke="#00a14b" stroke-width="2.4"/></svg>Tenant Referral Rewards</li>
    <li><svg width="19" height="19" viewBox="0 0 19 19" aria-hidden="true"><rect width="19" height="19" fill="#fff21f"/><path d="M4 10l4 4 8-9" fill="none" stroke="#00a14b" stroke-width="2.4"/></svg>Available Charts &amp; Dollies</li>
  </ul>
  <div class="abs boxes-art" role="img" aria-label="Illustration of a stack of four cardboard moving boxes"></div>

  <div class="abs call-bar">
    <svg width="180" height="48" viewBox="0 0 180 48" aria-hidden="true"><path d="M0 0H152L180 24L152 48H0Z" fill="#00a14b"/></svg>
  </div>
  <p class="abs call-label">Call Today !</p>
  <p class="abs call-number">317.555.4820</p>

  <div class="abs web-bar">
    <svg width="20" height="20" viewBox="0 0 24 24" aria-hidden="true" fill="none" stroke="#e41e26" stroke-width="1.8">
      <circle cx="12" cy="12" r="10"/><ellipse cx="12" cy="12" rx="4.5" ry="10"/><path d="M2 12h20M4 6.5h16M4 17.5h16"/>
    </svg>
    <span>www.tidylockeryard.example</span>
  </div>

  <div class="abs stamp-box"></div>
  <div class="abs address-rule" style="top:261px"></div>
  <div class="abs address-rule" style="top:292px"></div>
  <div class="abs address-rule" style="top:324px"></div>

  <div class="abs location" style="left:424px">
    <p class="location__name">Tidy Locker Yard</p>
    <p class="location__street">24815 Marlow Court Larkfield, IN 46901</p>
    <p class="location__phone"><svg width="13" height="13" viewBox="0 0 14 14" aria-hidden="true"><circle cx="7" cy="7" r="6.2" fill="none" stroke="#e41e26" stroke-width="1.2"/><path d="M4.6 3.8l1.4 1.6-.7.9a5 5 0 0 0 2.4 2.4l.9-.7 1.6 1.4-.9 1.1c-2.6-.3-5.2-2.9-5.5-5.5z" fill="#e41e26"/></svg>317.555.4820</p>
  </div>
  <div class="abs location" style="left:619px">
    <p class="location__name">Tidy Locker Yard</p>
    <p class="location__street">16200 Quenby Glen Road Brookvale, IN 46977</p>
    <p class="location__phone"><svg width="13" height="13" viewBox="0 0 14 14" aria-hidden="true"><circle cx="7" cy="7" r="6.2" fill="none" stroke="#e41e26" stroke-width="1.2"/><path d="M4.6 3.8l1.4 1.6-.7.9a5 5 0 0 0 2.4 2.4l.9-.7 1.6 1.4-.9 1.1c-2.6-.3-5.2-2.9-5.5-5.5z" fill="#e41e26"/></svg>317.555.7136</p>
  </div>
</section>

</body>
</html>
```